Pinewell Fitness

I am looking for a crisp/clean website That is simple. We are looking for membership page, about us, photos, and retail sale of out clothes and accessories.

Below is our logo.

Industry/Entity Type

Retail

Number of Pages Required

4 page

Font styles to use
Sans Serif

```html
<!DOCTYPE html>
<html lang="en">
<head>
<meta charset="utf-8">
<title>Pinewell Fitness</title>
<link rel="stylesheet" href="https://fonts.googleapis.com/css2?family=Arimo:wght@400;700&family=Play:wght@400;700&display=swap">
<style>
:root{
  --red:#b01f1a;
  --black:#000;
  --ink:#111;
  --white:#fff;
  --grey-box:rgba(200,200,200,.88);
  --hero-dark:#1b1b1b;
}
*{box-sizing:border-box;margin:0;padding:0}
html,body{width:970px;height:1200px;overflow:hidden;background:var(--white)}
body{position:relative;font-family:"Arimo",Arial,sans-serif;color:var(--ink)}
a{text-decoration:none}
.abs{position:absolute}

.site-header{left:0;top:0;width:970px;height:97px;background:var(--white)}
.brand{left:70px;top:31px;display:flex;align-items:center;gap:10px}
.brand-mark{width:22px;height:22px;border-radius:50%;background:var(--red)}
.brand-name{font-family:"Play",sans-serif;font-weight:700;font-size:26px;color:var(--ink);letter-spacing:1px}
.main-nav a,.footer-nav a{position:absolute;transform:translateX(-50%);font-family:"Play",sans-serif;font-size:15px;white-space:nowrap}
.main-nav a{top:38px;color:var(--ink)}
.main-nav a.active,.footer-nav a.active{color:var(--red)}

.hero{left:0;top:97px;width:970px;height:319px;background:radial-gradient(ellipse at 45% 25%,#6a6a6a 0%,#333 40%,var(--hero-dark) 100%)}
.hero-title{left:97px;top:136px;width:380px;text-align:center;color:var(--white);font-weight:400;font-size:34px;line-height:42px;text-shadow:0 2px 8px #000;white-space:nowrap}
.hero-box{left:500px;top:101px;width:407px;height:123px}
.hero-copy{left:515px;top:105px;width:370px;font-family:"Play",sans-serif;font-size:16.5px;line-height:25px;color:#222;white-space:nowrap}
.btn-hero{left:499px;top:241px;width:177px;height:42px;background:var(--white);color:var(--red);font-size:22px;display:flex;align-items:center;justify-content:center}

.promo{left:0;top:416px;width:970px;height:185px}
.promo-photo{left:0;top:0;width:540px;height:185px;background:linear-gradient(100deg,#3a2b3a 0%,#b98a7a 22%,#e9e6dc 45%,#d9d6c8 75%,#bdb9a6 100%)}
.promo-title{left:522px;top:16px;width:400px;text-align:center;color:var(--white);font-weight:400;font-size:27px;line-height:27px;white-space:nowrap}
.promo-copy{left:510px;top:75px;width:424px;text-align:center;color:var(--white);font-family:"Play",sans-serif;font-size:18px;line-height:25px;white-space:nowrap}
.btn-retail{left:628px;top:134px;width:152px;height:40px;border:2px solid var(--black);color:var(--black);font-size:19px;display:flex;align-items:center;justify-content:center}

.card{position:absolute;top:617px;width:290px;text-align:center}
.card-photo{margin:0 auto;width:196px;height:196px;border-radius:50%;border:3px solid var(--red)}
.photo-men{background:radial-gradient(ellipse 45% 60% at 50% 50%,#2b2b2b 0%,#4a4a4a 45%,#f4f4f4 80%)}
.photo-women{background:radial-gradient(ellipse 45% 60% at 50% 55%,#1c1c1c 0%,#c23a36 35%,#f3f3f3 80%)}
.photo-gift{background:radial-gradient(circle at 50% 45%,#e02a2a 0%,#e8e8e8 35%,#fff 70%)}
.card-head{height:64px;margin-top:8px}
.card-title{color:var(--red);font-family:"Play",sans-serif;font-weight:400;font-size:23px;line-height:29px;white-space:nowrap}
.card-sub{margin-top:3px;color:var(--red);font-family:"Play",sans-serif;font-size:14px;line-height:20px}
.card-copy{font-size:10.6px;line-height:17px;color:var(--ink);white-space:nowrap}
.card-btn{display:flex;margin:14px auto 0;width:152px;height:40px;border:2px solid var(--red);color:var(--red);font-size:16px;align-items:center;justify-content:center}

.subscribe{left:0;top:1015px;width:970px;height:85px;background:var(--red)}
.field{position:absolute;top:34px;height:25px;background:var(--white);font-size:11px;color:#999;padding:6px 7px}
.btn-subscribe{left:738px;top:27px;width:149px;height:36px;background:var(--black);color:var(--white);font-size:16px;display:flex;align-items:center;justify-content:center}

.site-footer{left:0;top:1100px;width:970px;height:100px;background:var(--black)}
.footer-nav a{top:13px;color:var(--white)}
.copyright{left:73px;top:63px;font-size:10.5px;color:var(--white)}
.copyright span{color:var(--red)}
.social{position:absolute;top:42px;width:44px;height:44px;border-radius:50%;border:3px solid var(--red);display:flex;align-items:center;justify-content:center}
.social svg{width:20px;height:20px}
</style>
</head>
<body>
<header class="site-header abs">
  <div class="brand abs"><span class="brand-mark"></span><span class="brand-name">Pinewell Fitness</span></div>
  <nav class="main-nav">
    <a class="active" href="#" style="left:447px">Home</a>
    <a href="#" style="left:562px">About Us</a>
    <a href="#" style="left:668px">Photo</a>
    <a href="#" style="left:763px">Shop</a>
    <a href="#" style="left:866px">Contact</a>
  </nav>
</header>

<section class="hero abs" role="img" aria-label="Athlete lifting dumbbells against a dark background">
  <h1 class="hero-title abs">GET IN YOUR BEST<br>SHAPE NOW!</h1>
  <svg class="hero-box abs" viewBox="0 0 407 123" aria-hidden="true"><polygon points="0,0 407,0 365,123 0,123" fill="var(--grey-box)"/></svg>
  <p class="hero-copy abs">Lorem Ipsum is simply dummy text of the<br>printing and typesetting industry. Lorem<br>Ipsum has been the industry's standard<br>dummy text.</p>
  <a class="btn-hero abs" href="#">SHOP NOW</a>
</section>

<section class="promo abs">
  <div class="promo-photo abs" role="img" aria-label="Woman stretching during a workout with earphones"></div>
  <svg class="abs" style="left:0;top:0" width="970" height="185" aria-hidden="true"><polygon points="534,0 970,0 970,185 486,185" fill="var(--red)"/></svg>
  <h2 class="promo-title abs">GET BETTER RESULTS &amp;<br>A TON OF FUN</h2>
  <p class="promo-copy abs">Lorem Ipsum simply dummy text of the<br>printing and typesetting industry.</p>
  <a class="btn-retail abs" href="#">Retail Sale</a>
</section>

<article class="card" style="left:48px">
  <div class="card-photo photo-men" role="img" aria-label="Two men in black sports clothing running"></div>
  <div class="card-head"><h3 class="card-title">MEN Fitness<br>Clothes &amp; Accesories</h3></div>
  <p class="card-copy">Lorem Ipsum s simply dummy text of the printing<br>and typesetting industry. Lorem Ipsum has been<br>the industry's standard dummy text.</p>
  <a class="card-btn" href="#">SHOP NOW</a>
</article>
<article class="card" style="left:337px">
  <div class="card-photo photo-women" role="img" aria-label="Two women in red tops and black fitness pants"></div>
  <div class="card-head"><h3 class="card-title">WOMEN Fitness<br>Clothes &amp; Accesories</h3></div>
  <p class="card-copy">Lorem Ipsum s simply dummy text of the printing<br>and typesetting industry. Lorem Ipsum has been<br>the industry's standard dummy text.</p>
  <a class="card-btn" href="#">SHOP NOW</a>
</article>
<article class="card" style="left:627px">
  <div class="card-photo photo-gift" role="img" aria-label="White gift box with a red ribbon"></div>
  <div class="card-head"><h3 class="card-title">Gift Voucher</h3><p class="card-sub">Lorem Ipsum s simply dummy text</p></div>
  <p class="card-copy">Lorem Ipsum s simply dummy text of the printing<br>and typesetting industry. Lorem Ipsum has been<br>the industry's standard dummy text.</p>
  <a class="card-btn" href="#">PURCHASE NOW</a>
</article>

<section class="subscribe abs">
  <div class="field" style="left:71px;width:269px">Enter your Email</div>
  <div class="field" style="left:357px;width:243px">Enter your Email</div>
  <a class="btn-subscribe abs" href="#">SUBSCRIBE</a>
</section>

<footer class="site-footer abs">
  <nav class="footer-nav">
    <a class="active" href="#" style="left:269px">Home</a>
    <a href="#" style="left:384px">About Us</a>
    <a href="#" style="left:491px">Photo</a>
    <a href="#" style="left:585px">Shop</a>
    <a href="#" style="left:689px">Contact</a>
  </nav>
  <p class="copyright abs">© <span>Pinewell Fitness</span> - 2014. All Rights Reserved.</p>
  <a class="social" href="#" style="left:741px" aria-label="Share">
    <svg viewBox="0 0 20 20" aria-hidden="true"><g fill="var(--white)"><circle cx="15" cy="4" r="3"/><circle cx="5" cy="10" r="3"/><circle cx="15" cy="16" r="3"/></g><path d="M15 4L5 10L15 16" stroke="var(--white)" stroke-width="2" fill="none"/></svg>
  </a>
  <a class="social" href="#" style="left:800px" aria-label="Message">
    <svg viewBox="0 0 20 20" aria-hidden="true"><path d="M2 3h16v11H8l-4 4v-4H2z" fill="var(--white)"/></svg>
  </a>
  <a class="social" href="#" style="left:859px" aria-label="Email">
    <svg viewBox="0 0 20 20" aria-hidden="true"><rect x="1" y="4" width="18" height="12" fill="var(--white)"/><path d="M1 4l9 7 9-7" stroke="var(--black)" stroke-width="1.6" fill="none"/></svg>
  </a>
</footer>
</body>
</html>
```